Most captivating card ever!

Life Coach - Professional Adventurer - Entrepreneur
I need the worlds most amazing business card for my personal brand. This business card will mostly be used to give to prospective clients for life coaching and business coaching.
Be creative, be adventurous. It needs to stand out. Make people say.. I need this guy!
My background is as an entrepreneur and professional adventurer undertaking extreme expeditions. I am now moving into life coaching.
No specific design ideas, so you have full creativity. Show me your best.
Industry/Entity Type
Life Coaching
Contact Information for Business Card
Dan Pellow
itsdanp.com.au
0468215903
Colors
Designer to choose colors to be used in the design.
Look and feel

```html
<!DOCTYPE html>
<html lang="en">
<head>
<meta charset="UTF-8">
<title>Dan Pellow – Business Card</title>
<link rel="stylesheet" href="https://fonts.googleapis.com/css2?family=Cinzel:wght@400;500&display=swap">
<style>
  :root {
    --page-bg: #e9e6e3;
    --frost-top: #f4f1ef;
    --frost-bottom: #e8e2df;
    --card-red: #ab2222;
    --name-red: #a81c1c;
    --title-grey: #3a3636;
    --icon-gold: #f1b40c;
    --contact-white: #fbf4f2;
  }
  * { margin: 0; padding: 0; box-sizing: border-box; }
  html, body {
    width: 1200px;
    height: 900px;
    overflow: hidden;
    background: var(--page-bg);
  }
  .business-card {
    position: absolute;
    left: 158px;
    top: 176px;
    width: 884px;
    height: 547px;
    box-shadow: 0 14px 40px rgba(0,0,0,0.18);
    font-family: "Cinzel", "Trajan Pro", serif;
  }
  .identity-panel {
    height: 297px;
    background: linear-gradient(180deg, var(--frost-top), var(--frost-bottom));
    text-align: center;
    position: relative;
  }
  .holder-name {
    position: absolute;
    left: 0; right: 0;
    top: 98px;
    font-size: 58px;
    font-weight: 500;
    letter-spacing: 2px;
    color: var(--name-red);
    line-height: 1;
  }
  .holder-title {
    position: absolute;
    left: 0; right: 0;
    top: 178px;
    font-size: 30px;
    font-weight: 400;
    letter-spacing: 2px;
    color: var(--title-grey);
    line-height: 1;
  }
  .contact-panel {
    height: 250px;
    background: var(--card-red);
    position: relative;
    text-align: center;
    color: var(--contact-white);
  }
  .contact-icons {
    position: absolute;
    top: 43px;
    left: 0; right: 0;
    display: flex;
    justify-content: center;
    gap: 12px;
  }
  .contact-icon {
    width: 46px;
    height: 46px;
    border-radius: 6px;
    background: var(--icon-gold);
    display: flex;
    align-items: center;
    justify-content: center;
  }
  .contact-line {
    position: absolute;
    left: 0; right: 0;
    font-size: 29px;
    letter-spacing: 1px;
    line-height: 1;
  }
  .contact-phone { top: 117px; }
  .contact-web { top: 155px; text-transform: uppercase; font-size: 27px; }
</style>
</head>
<body>
  <div class="business-card">
    <div class="identity-panel">
      <h1 class="holder-name">Dan Pellow</h1>
      <p class="holder-title">Managing Director</p>
    </div>
    <div class="contact-panel">
      <div class="contact-icons">
        <span class="contact-icon" aria-label="Phone">
          <svg width="28" height="22" viewBox="0 0 28 22" aria-hidden="true">
            <path d="M2 8 Q14 -1 26 8 L22 11 L19 7 Q14 5 9 7 L6 11 Z" fill="#fff"/>
            <path d="M7 12 L9 9 H19 L21 12 V20 H7 Z" fill="#fff"/>
            <circle cx="14" cy="15" r="2.5" fill="#f1b40c"/>
          </svg>
        </span>
        <span class="contact-icon" aria-label="Website">
          <svg width="28" height="28" viewBox="0 0 28 28" aria-hidden="true">
            <circle cx="14" cy="14" r="11" fill="#fff"/>
            <path d="M9 7 Q13 9 12 13 Q9 15 10 19 L7 17 Q5 12 9 7 Z M16 6 Q21 9 20 14 Q17 16 18 21 L15 22 Q14 17 16 14 Q14 10 16 6 Z" fill="#f1b40c"/>
          </svg>
        </span>
      </div>
      <p class="contact-line contact-phone">0468215903</p>
      <p class="contact-line contact-web">www.itsdanp.com.au</p>
    </div>
  </div>
</body>
</html>
```